Mend and secure Word doc project

Mend & Secure are an established home appliance repair and warranty provider looking to rebrand the letters sent to our customers with a new and fresh design.
Please refer to our website for our colour scheme and logo which we are not looking to change:
www.mendandsecure.co.uk
The letters which we are looking to have redesigned are:
Welcome letters / confirmation paperwork
Basic letter template
Welcome letters:
Page 1 – Opening / Welcome
Page 2 – Plan documentation details
Page 3 & 4 – Terms & Conditions
We can provide a copy of our current welcome / confirmation letters but as we are looking for full redesign, we are looking to steer away from what we have been using historically.
We will be running further projects and we are looking to use the same designer which we pick from this competition so please consider this when submitting your designs.
UPDATE - 01/11/23
An example of our current Welcome documentation has been uploaded for the purpose of example of the placement of the content. As per the brief, we are not looking for a similar design but purely uploading the current documentation to give you an idea of what we are currently using.
Look and feel
Each slider illustrates characteristics of the customer's brand and the style your logo design should communicate.

```html
<!DOCTYPE html>
<html lang="en">
<head>
<meta charset="utf-8">
<title>Mend &amp; Secure – Letter Suite</title>
<link rel="stylesheet" href="https://fonts.googleapis.com/css2?family=Jost:wght@400;500&family=Tinos&display=swap">
<style>
  :root {
    --blue: #003399;
    --teal: #2a9a80;
    --green: #5cf06e;
    --paper: #dcdcdc;
    --ink: #1e1e1e;
    --footer-green: #5cff6e;
    --white: #ffffff;
  }
  * { margin: 0; padding: 0; box-sizing: border-box; }
  html, body { width: 1200px; height: 1200px; overflow: hidden; }
  body {
    position: relative;
    font-family: "Jost", sans-serif;
    background: linear-gradient(to top right, var(--blue) 0%, #0d5a92 35%, var(--teal) 60%, var(--green) 100%);
  }
  .sheet {
    position: absolute;
    background: var(--paper);
    overflow: hidden;
  }
  .sheet--brand {
    background: linear-gradient(to top right, #5cff6e 0%, #27a07a 25%, #0a5f98 55%, var(--blue) 80%);
  }
  .sheet__header {
    height: 50px;
    background: linear-gradient(to top right, #5cff6e 0%, #2ca67a 30%, #0c5898 60%, var(--blue) 90%);
    color: var(--white);
    font-size: 13.5px;
    font-weight: 400;
    letter-spacing: 0.3px;
    padding: 14px 0 0 25px;
  }
  .sheet__body {
    position: absolute;
    left: 31px;
    right: 36px;
    top: 66px;
    color: var(--ink);
    font-size: 5.2px;
    line-height: 1.25;
  }
  .sheet__body p { margin-bottom: 8px; text-align: justify; }
  .sheet__body p.tight { margin-bottom: 0; }
  .sheet__body ul { list-style: none; margin-bottom: 8px; }
  .sheet__body li { margin-bottom: 2.5px; }
  .letter-date { text-align: right !important; }
  .sheet__footer {
    position: absolute;
    bottom: 12px;
    left: 0; right: 0;
    display: flex;
    justify-content: center;
    gap: 26px;
    font-family: "Tinos", serif;
    font-size: 5px;
    color: var(--footer-green);
  }
  .brand-name {
    position: absolute;
    left: 0; right: 0;
    top: 148px;
    text-align: center;
    color: var(--white);
    font-size: 11px;
    font-weight: 400;
    letter-spacing: 0.6px;
  }
  .brand-dot {
    display: block;
    width: 16px; height: 16px;
    margin: 0 auto 8px;
    border-radius: 50%;
    background: var(--white);
  }
</style>
</head>
<body>

  <section class="sheet sheet--brand cover" style="left:68px;top:166px;width:286px;height:378px;">
    <div class="brand-name"><span class="brand-dot"></span>MEND &amp; SECURE</div>
  </section>

  <section class="sheet welcome" style="left:450px;top:166px;width:287px;height:370px;">
    <header class="sheet__header">Welcome Letter</header>
    <div class="sheet__body" style="top:67px;">
      <p class="letter-date">[Date]</p>
      <p>Dear [Customer's Name],</p>
      <p>We are delighted to welcome you to Mend &amp; Secure!</p>
      <p>At Mend &amp; Secure, we understand the importance of keeping your home appliances running smoothly. Our mission is to provide you with top-notch appliance repair and warranty services. We're excited to have you as a valued customer, and we're committed to delivering exceptional service.</p>
      <p>Whether you need a quick repair or have chosen one of our comprehensive warranty plans, we are here to support you every step of the way. You can rely on us to keep your appliances in great working condition.</p>
      <p>Should you have any questions or require assistance, please don't hesitate to reach out to our dedicated customer support team. We're here to help!</p>
      <p>Thank you for choosing Mend &amp; Secure. We look forward to serving you.</p>
      <p>Sincerely,</p>
      <p class="tight">[Your Name]</p>
      <p>[Your Title]</p>
    </div>
    <footer class="sheet__footer"><span>www.website.com</span><span>info@email.com</span><span>543-PhoneNumber</span></footer>
  </section>

  <section class="sheet documentation" style="left:832px;top:175px;width:273px;height:366px;">
    <header class="sheet__header">Documentation</header>
    <div class="sheet__body" style="top:66px;">
      <p class="letter-date">[Date]</p>
      <p>Dear [Customer's Name],</p>
      <p>Here are the details of your Mend &amp; Secure plan:</p>
      <ul>
        <li>- Plan Name: [Plan Name]</li>
        <li>- Coverage Details: [Coverage Details]</li>
        <li>- Covered Appliances: [List of Covered Appliances]</li>
        <li>- Plan Identification/Reference Number: [Plan ID/Ref Number]</li>
        <li>- Effective Date: [Effective Date]</li>
        <li>- Expiry Date: [Expiry Date]</li>
      </ul>
      <p>Your plan is designed to give you peace of mind, knowing that your essential appliances are protected. We'll be there to ensure quick and reliable repairs whenever you need them.</p>
      <p>Please keep this document for your records. If you have any questions or require service, please reach out to our customer support team.</p>
      <p>Thank you for choosing Mend &amp; Secure. We're here to keep your appliances running smoothly!</p>
      <p>Sincerely,</p>
      <p class="tight">[Your Name]</p>
      <p>[Your Title]</p>
    </div>
    <footer class="sheet__footer"><span>www.website.com</span><span>info@email.com</span><span>543-PhoneNumber</span></footer>
  </section>

  <section class="sheet terms" style="left:69px;top:608px;width:285px;height:369px;">
    <header class="sheet__header">Terms &amp; Condition</header>
    <div class="sheet__body" style="top:65px;">
      <p class="letter-date">[Date]</p>
      <p>Dear [Customer's Name],</p>
      <p>TERMS &amp; CONDITIONS OF YOUR MEND &amp; SECURE PLAN</p>
      <p>These terms and conditions ("Terms") outline the agreement between you, the customer, and Mend &amp; Secure for your appliance repair and warranty plan. By subscribing to our services, you agree to the following:</p>
      <p class="tight">[Detailed terms and conditions specific to your plan. This should include coverage details, service limitations, claim procedures, responsibilities of the customer, and any other relevant information. Ensure that the language is clear, concise, and legally compliant.]</p>
      <p class="tight">[Detailed terms and conditions specific to your plan. This should include coverage details, service limitations, claim procedures, responsibilities of the customer, and any other relevant information. Ensure that the language is clear, concise, and legally compliant.]</p>
      <p class="tight">[Detailed terms and conditions specific to your plan. This should include coverage details, service limitations, claim procedures, responsibilities of the customer, and any other relevant information. Ensure that the language is clear, concise, and legally compliant.]</p>
      <p class="tight">[Detailed terms and conditions specific to your plan. This should include coverage details, service limitations, claim procedures, responsibilities of the customer, and any other relevant information. Ensure that the language is clear, concise, and legally compliant.]</p>
      <p class="tight">[Detailed terms and conditions specific to your plan. This should include coverage details, service limitations, claim procedures, responsibilities of the customer, and any other relevant information. Ensure that the language is clear, concise, and legally compliant.]</p>
    </div>
    <footer class="sheet__footer"><span>www.website.com</span><span>info@email.com</span><span>543-PhoneNumber</span></footer>
  </section>

  <section class="sheet terms-sign" style="left:466px;top:625px;width:270px;height:370px;">
    <header class="sheet__header">Terms &amp; Conditions</header>
    <div class="sheet__body" style="top:68px;">
      <p>Please review these terms carefully. If you have any questions or concerns, please contact our customer support team for clarification.</p>
      <p>By signing below, you acknowledge that you have received, read, and understood these Terms and agree to abide by them.</p>
      <p>Customer's Signature: ______________________ Date: ____________</p>
      <p>Thank you for choosing Mend &amp; Secure. We're committed to providing you with the best appliance repair and warranty services.</p>
      <p>Sincerely,</p>
      <p>[Your Name]</p>
    </div>
    <footer class="sheet__footer"><span>www.website.com</span><span>info@email.com</span><span>543-PhoneNumber</span></footer>
  </section>

  <section class="sheet sheet--brand back-cover" style="left:832px;top:625px;width:286px;height:370px;"></section>

</body>
</html>
```